Tomuvin 30ml pipette jar Mental Health

Label and Box for 30ml amber jar with pipette.
Already have a sample design, that needs to be adapted and possibly improved for the new packaging.
Dark brown letters on White Label.
The jar 30ml with pipette / dropper is amber with dark cap. Please view the photo.
Please view all the files, which I am uploading.
Please provide a mock up version.
Thank you.

Target Market(s)

Upscale women 34-59

Industry/Entity Type

Nutrition, Medical

Requirements
Must have
• Conservative, Minimalistic, Luxury
Should not have
• Leaves

```html
<!DOCTYPE html>
<html lang="en">
<head>
<meta charset="utf-8">
<title>Tomuvin – Box and Label</title>
<link rel="stylesheet" href="https://fonts.googleapis.com/css2?family=Rubik:wght@400;500;600&display=swap">
<style>
  :root {
    --backdrop: #d8d5ce;
    --panel-front: #e4e5ef;
    --panel-side: #1f1f21;
    --label-white: #ffffff;
    --ink: #1a1a1a;
    --ink-soft: #3a3a3a;
    --side-ink: #8a8a8a;
    --band: #2a2a2c;
    --band-text: #d6d6d6;
    --gold: #b08a4e;
  }
  * { box-sizing: border-box; margin: 0; padding: 0; }
  html, body {
    width: 1200px; height: 675px; overflow: hidden;
    background: var(--backdrop);
    font-family: "Rubik", Arial, sans-serif;
    color: var(--ink);
  }
  .stage {
    position: relative; width: 1200px; height: 675px;
    display: flex; align-items: center; justify-content: center; gap: 70px;
  }

  /* Carton: side panel + front panel */
  .carton { display: flex; height: 560px; }
  .carton-side {
    width: 74px; height: 100%;
    background: var(--panel-side);
    position: relative; overflow: hidden;
  }
  .side-copy {
    position: absolute; top: 30px; left: 50%;
    width: 420px;
    transform-origin: top left;
    transform: rotate(90deg) translateY(-50%);
    color: var(--side-ink); font-size: 7px; line-height: 1.6; letter-spacing: 0.02em;
    margin-left: 0;
  }
  .side-copy h3 { font-size: 7px; font-weight: 500; margin-bottom: 6px; }
  .side-copy p { margin-bottom: 8px; }

  .carton-front {
    width: 210px; height: 100%;
    background: var(--panel-front);
    display: flex; flex-direction: column;
    position: relative;
  }

  /* Shared panel content */
  .brand {
    display: flex; align-items: center; gap: 8px;
    font-size: 15px; font-weight: 400; color: var(--ink);
  }
  .brand-dot { width: 20px; height: 20px; border-radius: 50%; background: var(--gold); flex: none; }
  .product-name {
    font-weight: 600; letter-spacing: 0.01em; color: var(--ink);
  }
  .name-rule { height: 1.5px; background: var(--ink); }
  .claim { color: var(--ink-soft); line-height: 1.25; }
  .claim strong { display: block; font-weight: 600; color: var(--ink); }
  .volume-band {
    background: var(--band); color: var(--band-text);
    display: flex; align-items: center; justify-content: center;
    font-size: 12px; font-weight: 400;
  }

  .carton-front .brand { margin: 72px 0 0 18px; }
  .carton-front .product-name { font-size: 32px; margin: 210px 0 0 18px; }
  .carton-front .name-rule { width: 100px; margin: 10px 0 0 20px; }
  .carton-front .claim { font-size: 10px; margin: 160px 0 0 18px; }
  .carton-front .volume-band { margin-top: auto; height: 58px; }

  /* Bottle label, flat */
  .bottle-label {
    width: 300px; height: 330px;
    background: var(--label-white);
    display: flex; flex-direction: column;
  }
  .bottle-label .brand { margin: 40px 0 0 30px; font-size: 16px; }
  .bottle-label .product-name { font-size: 40px; margin: 40px 0 0 30px; }
  .bottle-label .name-rule { width: 120px; margin: 10px 0 0 32px; }
  .bottle-label .claim { font-size: 11px; margin: 40px 0 0 30px; }
  .bottle-label .volume-band { margin-top: auto; height: 52px; font-size: 13px; }
</style>
</head>
<body>
<main class="stage">
  <section class="carton" aria-label="Tomuvin carton">
    <div class="carton-side">
      <div class="side-copy">
        <h3>Directions for use</h3>
        <p>Take one full dropper daily with water or as advised by your practitioner.</p>
        <p>Store in a cool dry place away from direct light. Keep out of reach of children.</p>
        <p>Shake gently before each use.</p>
        <p>Do not exceed the stated dose.</p>
      </div>
    </div>
    <div class="carton-front">
      <div class="brand"><span class="brand-dot"></span><span>Vela Clinics</span></div>
      <h1 class="product-name">TOMUVIN</h1>
      <div class="name-rule"></div>
      <p class="claim"><strong>Doctor Formulated</strong>Developed in Clinical Practice</p>
      <div class="volume-band">30ml</div>
    </div>
  </section>

  <section class="bottle-label" aria-label="Tomuvin bottle label">
    <div class="brand"><span class="brand-dot"></span><span>Vela Clinics</span></div>
    <h2 class="product-name">TOMUVIN</h2>
    <div class="name-rule"></div>
    <p class="claim"><strong>Doctor Formulated</strong>Developed in Clinical Practice</p>
    <div class="volume-band">30ml</div>
  </section>
</main>
</body>
</html>
```